Talbrin Business Cards

Front and back. Simon Kavelle MBA is the CEO of Talbrin Homes. Black white and grays. Logo and cool design.

Target Market(s)

Professional lenders and investors

Industry/Entity Type

Real estate developer. NO HOUSES OR ROOFS

Contact Information for Business Card

Logo, name and unique design. Front and back. Simon Kavelle MBA is the CEO of Talbrin Homes. Black white and grays. Logo and cool design.

Font styles to use
Sans Serif

Colors

Designer to choose only greyscale colors for use in the design.

Requirements
Must have
• Cool look. Not the same card I could design.
Nice to have
• Something memorable
Should not have
• Basic

```html
<!DOCTYPE html>
<html lang="en">
<head>
<meta charset="utf-8">
<title>Talbrin Homes Business Cards</title>
<link rel="stylesheet" href="https://fonts.googleapis.com/css2?family=Montserrat:wght@800&family=Arimo:wght@400;700&display=swap">
<style>
  :root {
    --stage: #3b3b3b;
    --card-front: #2b2b2b;
    --card-back-dark: #0a0a0a;
    --card-back-mid: #1e1e1e;
    --card-back-light: #555555;
    --ink-white: #ffffff;
    --ink-soft: #e6e6e6;
    --divider: #5a5a5a;
  }
  * { box-sizing: border-box; margin: 0; padding: 0; }
  html, body {
    width: 1200px; height: 793px; overflow: hidden;
    background: var(--stage);
  }
  .canvas {
    position: relative; width: 1200px; height: 793px;
    background: var(--stage);
  }
  .card {
    position: absolute; width: 540px; height: 309px;
    border-radius: 3px;
    box-shadow: 0 14px 30px rgba(0,0,0,0.45);
    overflow: hidden;
  }
  .card--front {
    left: 45px; top: 150px;
    background: var(--card-front);
  }
  .card--back {
    left: 615px; top: 334px;
  }
  .wordmark {
    position: absolute;
    font-family: "Montserrat", sans-serif;
    font-weight: 800;
    color: var(--ink-white);
    letter-spacing: -0.5px;
    white-space: nowrap;
    line-height: 1;
  }
  .card--front .wordmark {
    left: 36px; top: 140px; font-size: 27px;
  }
  .divider {
    position: absolute; left: 290px; top: 40px;
    width: 1px; height: 229px;
    background: linear-gradient(to bottom, transparent, var(--divider) 20%, var(--divider) 80%, transparent);
  }
  .contact {
    position: absolute; left: 312px; top: 48px;
    font-family: "Arimo", sans-serif;
    color: var(--ink-soft);
    font-size: 13px; line-height: 1.35;
  }
  .contact__name {
    font-weight: 700; font-size: 17px; color: var(--ink-white);
  }
  .contact__title { margin-bottom: 12px; }
  .contact__address { margin-bottom: 12px; }
  .contact__list { list-style: none; }
  .contact__list li {
    display: flex; align-items: center; gap: 7px;
  }
  .contact__list svg { width: 11px; height: 11px; flex: none; }
  .pattern-field {
    position: absolute; inset: 0;
    background:
      repeating-linear-gradient(-16deg, rgba(255,255,255,0) 0px, rgba(255,255,255,0) 22px, rgba(255,255,255,0.06) 22px, rgba(255,255,255,0.06) 24px, rgba(255,255,255,0) 24px, rgba(255,255,255,0) 38px),
      radial-gradient(ellipse at 92% 40%, rgba(255,255,255,0.22), rgba(255,255,255,0) 55%),
      linear-gradient(110deg, var(--card-back-dark) 0%, var(--card-back-mid) 45%, var(--card-back-light) 100%);
  }
  .card--back .wordmark {
    left: 300px; top: 196px; font-size: 26px;
  }
</style>
</head>
<body>
<main class="canvas">
  <section class="card card--front" aria-label="Business card front">
    <div class="wordmark">Talbrin Homes</div>
    <div class="divider"></div>
    <div class="contact">
      <p class="contact__name">Simon Kavelle MBA</p>
      <p class="contact__title">CEO</p>
      <p class="contact__address">4120 Ridgeview Court<br>Fairbanks, Alaska 99712</p>
      <ul class="contact__list">
        <li>
          <svg viewBox="0 0 12 12" aria-hidden="true"><path d="M3 1 L5 3.5 L4 5 Q5 7 7 8 L8.5 7 L11 9 L9.5 11 Q4 10.5 1 2.5 Z" fill="#fff"/></svg>
          555-214-0187
        </li>
        <li>
          <svg viewBox="0 0 12 12" aria-hidden="true"><rect x="3" y="0.8" width="6" height="10.4" rx="1" fill="none" stroke="#fff" stroke-width="1.2"/><circle cx="6" cy="9.3" r="0.6" fill="#fff"/></svg>
          555-309-6642
        </li>
        <li>
          <svg viewBox="0 0 12 12" aria-hidden="true"><rect x="0.8" y="2.5" width="10.4" height="7" fill="none" stroke="#fff" stroke-width="1.2"/><path d="M1 3 L6 7 L11 3" fill="none" stroke="#fff" stroke-width="1.2"/></svg>
          info@talbrinhomes.com
        </li>
        <li>
          <svg viewBox="0 0 12 12" aria-hidden="true"><circle cx="6" cy="6" r="5" fill="none" stroke="#fff" stroke-width="1.2"/><ellipse cx="6" cy="6" rx="2.2" ry="5" fill="none" stroke="#fff" stroke-width="1"/><path d="M1 6 H11" stroke="#fff" stroke-width="1"/></svg>
          www.talbrinhomes.com
        </li>
      </ul>
    </div>
  </section>

  <section class="card card--back" aria-label="Business card back">
    <div class="pattern-field" role="img" aria-label="Repeating embossed company name pattern in gloss greys, dark on the left fading to light on the right"></div>
    <div class="wordmark">Talbrin Homes</div>
  </section>
</main>
</body>
</html>
```